Law Office Business Card

We need a business card design to include the following information:
Name of Firm: Brennick Law Group, P.A.
Address: 4627 Sandlot Ave, Ste 208, Coral Haven, FL 34990
Phone: 561-555-0148
Fax: 561-555-0193
Website: http://www.tbrennicklaw.example

We Need a place for the Person's name and email address. Please start with the following:
Lorna K. Dwyer, Esq.
lorna@tbrennicklaw.example

```html
<!DOCTYPE html>
<html lang="en">
<head>
<meta charset="utf-8">
<title>Brennick Law Group – Business Card</title>
<link href="https://fonts.googleapis.com/css2?family=Cormorant+Garamond:wght@400&family=Arimo:wght@400;700&display=swap" rel="stylesheet">
<style>
  :root {
    --backdrop: #e9e6e1;
    --card: #ffffff;
    --navy: #0b5582;
    --taupe: #a59686;
    --ink: #1c1c1c;
    --rule: #0b5582;
    --frame: #d9d4cd;
  }
  * { box-sizing: border-box; margin: 0; padding: 0; }
  html, body {
    width: 1200px; height: 780px; overflow: hidden;
    background: var(--backdrop);
  }
  .stage {
    position: relative; width: 1200px; height: 780px;
    display: flex; align-items: center; justify-content: center;
  }
  .card {
    position: relative; width: 980px; height: 560px;
    background: var(--card);
    box-shadow: 0 10px 30px rgba(0,0,0,.18);
    overflow: hidden;
  }
  .card__band {
    position: absolute; left: 0; top: 0; bottom: 0; width: 300px;
    background: var(--navy);
  }
  .card__mark-box {
    position: absolute; left: 70px; top: 60px; width: 250px; height: 250px;
    background: var(--card);
    border: 1px solid var(--frame);
  }
  .firm {
    position: absolute; left: 360px; top: 70px;
    font-family: "Cormorant Garamond", Georgia, serif;
    font-weight: 400; color: var(--taupe);
  }
  .firm__name { font-size: 64px; line-height: 1; letter-spacing: 1px; text-transform: uppercase; }
  .firm__sub { font-size: 24px; letter-spacing: 22px; text-transform: uppercase; margin-top: 12px; padding-left: 150px; }
  .attorney {
    position: absolute; left: 360px; top: 236px;
    font-family: "Arimo", Arial, sans-serif; font-weight: 700;
    font-size: 30px; color: var(--taupe);
  }
  .divider {
    position: absolute; left: 360px; top: 284px; width: 590px; height: 2px;
    background: var(--rule);
  }
  .contact {
    position: absolute; left: 360px; top: 302px;
    font-family: "Arimo", Arial, sans-serif; font-size: 24px;
    color: var(--ink); line-height: 35px; list-style: none;
  }
  .contact__line { display: flex; align-items: center; gap: 12px; }
  .contact__icon {
    width: 26px; height: 26px; background: var(--navy);
    display: inline-flex; align-items: center; justify-content: center;
  }
  .contact__icon svg { width: 18px; height: 18px; }
  .website {
    position: absolute; right: 40px; bottom: 34px;
    font-family: "Arimo", Arial, sans-serif; font-size: 24px; color: var(--ink);
  }
</style>
</head>
<body>
<main class="stage">
  <article class="card">
    <div class="card__band"></div>
    <div class="card__mark-box"></div>

    <header class="firm">
      <div class="firm__name">Brennick Law</div>
      <div class="firm__sub">Group</div>
    </header>

    <div class="attorney">Lorna K. Dwyer, Esq.</div>
    <div class="divider"></div>

    <ul class="contact">
      <li class="contact__line">4627 Sandlot Ave, Ste 208</li>
      <li class="contact__line">Coral Haven, FL 34990</li>
      <li class="contact__line">
        <span class="contact__icon">
          <svg viewBox="0 0 18 18"><path d="M5 2h3l1 4-2 1c1 2 2 3 4 4l1-2 4 1v3c0 1-1 2-2 2C8 15 3 10 3 4c0-1 1-2 2-2z" fill="#fff"/></svg>
        </span>561-555-0148
      </li>
      <li class="contact__line">
        <span class="contact__icon">
          <svg viewBox="0 0 18 18"><rect x="5" y="2" width="8" height="5" fill="#fff"/><rect x="2" y="7" width="14" height="6" fill="#fff"/><rect x="5" y="11" width="8" height="5" fill="#fff" stroke="#0b5582"/></svg>
        </span>561-555-0193
      </li>
      <li class="contact__line">
        <span class="contact__icon">
          <svg viewBox="0 0 18 18"><rect x="2" y="4" width="14" height="10" fill="none" stroke="#fff" stroke-width="1.5"/><path d="M2 4l7 6 7-6" fill="none" stroke="#fff" stroke-width="1.5"/></svg>
        </span>lorna@tbrennicklaw.example
      </li>
    </ul>

    <div class="website">www.tbrennicklaw.example</div>
  </article>
</main>
</body>
</html>
```